Professional Engineering Web Design

Project Brief: Website Redesign for Mechanical Design Consultancy
Project Overview
I want to update and improve my current website to create a more professional, modern, and high-credibility online presence for my mechanical design consultancy.

Current site: https://valtrobuild.design/

The new website must communicate expertise, precision, and trust—matching the standard of top engineering and product design agencies.

Reference Websites (Style + Structure Inspiration)
These represent the quality, cleanliness, and professionalism I want to achieve:

https://plinthformworks.com/
https://www.zorvanta.com/
https://quellory-uk.com/
Brand Look
Professional, modern, engineering-focused aesthetic
Clean layouts and strong typography
High-quality imagery conveying precision, innovation, and mechanical expertise
Colour scheme and styling must follow my existing logo (attached in project)
Platform Requirements
The website must be built on WordPress
Should use a clean, flexible theme or modern page builder (Elementor, Gutenberg, Bricks, or similar)
Avoid overly complex custom coding so I can easily edit content later
Final deliverable must allow me to manage and update content without developer assistance
Functionality
Fast-loading, lightweight, and smooth user experience
Clean animations and transitions similar to the reference sites
Fully mobile responsive
Clear navigation and strong visual hierarchy
Contact forms optimised for lead generation
Optional: subtle scroll effects, case study sliders, icon animations, etc.
SEO Aspirations
Developer should recommend and implement a modern SEO strategy
Proper on-page SEO setup (titles, meta, schema, alt tags, heading structure)
Optimised site architecture for ranking and crawling
Aim: Generate leads through improved visibility and keyword targeting
Optional but useful: Google Analytics, Google Search Console setup
User Journeys
(Recommended structure)

The site should be crafted around clear, intuitive journeys for each type of visitor:

Potential new clients
Quickly understand what services I offer
View examples of past work / case studies
See credibility indicators (process, expertise, industries served)
Easily contact me or request a project discussion
Returning clients
Access updated portfolio items
Find contact details or book follow-up work easily
General visitors discovering through SEO
Be guided to valtro service areas
Understand my value proposition quickly
Be invited to learn more or make contact
The developer should design the structure to support these journeys smoothly.

Maintenance Expectations
Website will be maintained by me, so it should be easy to update using relatively basic WordPress skills
Use modular templates and simple backend structure
Avoid unnecessary plugins
Provide brief handover documentation if required
Hosting Preferences
Site is currently hosted via a family member
Open to discussing moving to a paid, reliable hosting provider if preferable for performance and maintainability
Developer may advise on the best hosting setup for WordPress
Content
Most content can be taken from the existing website
Developer is welcome to suggest improvements to structure, layout, and imagery
Must remain easy for me to edit or add new content later (e.g., new projects)
Deliverables
Fully built WordPress website
Clean, professional, modern design inspired by the reference sites
Mobile-responsive across all devices
SEO-ready structure and optimisations
Transfer of website and admin rights
Any design assets, templates, or documentation used

```html
<!DOCTYPE html>
<html lang="en">
<head>
<meta charset="utf-8">
<title>Valtro Mechanical Design</title>
<link href="https://fonts.googleapis.com/css2?family=Inter:wght@400;500;600;700;800&display=swap" rel="stylesheet">
<style>
:root{
  --blue:#1a56ff;
  --ink:#0b0b0c;
  --dark:#0a0a0b;
  --panel:#17181b;
  --line:#26272b;
  --muted:#8a8c93;
  --text:#4b4d53;
  --soft:#f7f7f8;
  --card:#fafafa;
  --border:#ececee;
  --white:#ffffff;
}
*{box-sizing:border-box;margin:0;padding:0}
html,body{width:1200px;height:1200px;overflow:hidden;background:var(--white);font-family:'Inter',sans-serif;color:var(--ink)}
.page{position:absolute;left:507px;top:0;width:1200px;height:7728px;transform:scale(0.15528);transform-origin:0 0;background:var(--white)}
section,footer{position:absolute;left:0;width:1200px;overflow:hidden}
.abs{position:absolute}
.label{font-size:12px;font-weight:700;letter-spacing:.12em;color:var(--blue);text-transform:uppercase}
.h2{font-size:54px;font-weight:700;letter-spacing:-.03em;line-height:1.05}
.lead{font-size:17px;line-height:1.6;color:var(--text)}

/* hero */
.hero{top:0;height:972px;background:radial-gradient(ellipse 600px 500px at 1000px 420px,#101a3a 0%,transparent 70%),linear-gradient(180deg,#07070a,#0b0c12 70%,#060608);color:var(--white)}
.nav{top:20px;left:28px;right:28px;height:32px;display:flex;align-items:center}
.brand{display:flex;align-items:center;gap:10px;font-size:26px;font-weight:600;letter-spacing:.06em}
.brand-dot{width:26px;height:26px;border-radius:50%;background:currentColor}
.nav-links{position:absolute;left:420px;display:flex;gap:34px;font-size:14px;color:#cfd0d4}
.nav-cta{position:absolute;right:0;background:var(--white);color:var(--ink);font-size:13px;font-weight:600;padding:9px 22px;border-radius:20px}
.hero-badge{left:28px;top:120px;font-size:12px;color:#8aa6ff;background:#101a3a;border:1px solid #1c2c66;padding:7px 16px;border-radius:20px}
.hero-title{left:28px;top:180px;font-size:66px;font-weight:700;letter-spacing:-.035em;line-height:1.09}
.hero-title .accent{color:var(--blue)}
.hero-copy{left:28px;top:428px;width:520px;font-size:18px;line-height:1.65;color:#9aa0b5}
.btn-blue{background:var(--blue);color:var(--white);font-size:14px;font-weight:600;padding:14px 26px;border-radius:30px}
.hero-btns{left:28px;top:566px;display:flex;align-items:center;gap:28px}
.hero-btns .ghost{font-size:14px;font-weight:600;color:var(--white)}
.stats{left:28px;top:676px;display:flex;gap:32px}
.stat b{display:block;font-size:32px;font-weight:700}
.stat span{font-size:12px;color:var(--muted)}
.tablet{left:684px;top:216px;width:420px;height:424px;background:#f2f2f3;border-radius:22px;padding:22px}
.tablet .screen{width:100%;height:100%;border-radius:8px;background:radial-gradient(circle at 50% 55%,#5a5c62,#2b2c30 45%,#18191c)}
.float-card{background:rgba(40,42,48,.92);border:1px solid #3a3c44;border-radius:12px;color:var(--white);font-size:12px;padding:12px 16px;display:flex;gap:10px;align-items:center}
.float-card i{width:22px;height:22px;border-radius:6px;display:block;flex:none}
.float-card small{display:block;color:var(--muted);font-size:10px}
.industries{left:0;top:812px;width:1200px;border-top:1px solid #1a1b20;text-align:center;padding-top:32px}
.industries p{font-size:11px;letter-spacing:.16em;color:#5d6068}
.industries ul{list-style:none;display:flex;justify-content:center;gap:56px;margin-top:24px;font-size:14px;color:#6a6d75}

/* services */
.services{top:972px;height:1128px}
.svc-grid{left:28px;top:328px;width:1144px;display:grid;grid-template-columns:368px 368px 372px;grid-template-rows:216px 216px 216px;column-gap:18px;row-gap:16px}
.svc{background:var(--card);border:1px solid var(--border);border-radius:14px;padding:30px}
.svc .ico{width:44px;height:44px;border-radius:10px;background:#e8eeff;display:flex;align-items:center;justify-content:center;margin-bottom:28px}
.svc h3{font-size:19px;font-weight:600;margin-bottom:12px}
.svc p{font-size:13px;line-height:1.6;color:var(--muted);width:280px}
.svc.featured{background:var(--dark);border-color:var(--dark);color:var(--white);grid-row:span 2}
.svc.featured .ico{background:#1b2440}
.svc.featured p{color:#b8bac0}
.svc .tag{margin-top:24px;padding-top:18px;border-top:1px solid var(--line);font-size:12px;color:#6a6d75}

/* projects */
.projects{top:2100px;height:2048px;background:var(--soft)}
.filters{right:28px;top:180px;display:flex;gap:10px;font-size:12px;color:var(--text)}
.filters span{padding:8px 14px;border-radius:20px}
.filters .on{background:var(--ink);color:var(--white)}
.proj{border-radius:12px;overflow:hidden}
.proj .chip{position:absolute;left:20px;top:20px;background:var(--white);color:var(--ink);font-size:11px;font-weight:600;padding:5px 12px;border-radius:14px}
.more{left:0;width:1200px;top:1896px;text-align:center;font-size:14px;font-weight:600}

/* process */
.process{top:4148px;height:980px;background:var(--dark);color:var(--white)}
.step{left:28px;width:548px;display:flex;gap:24px;align-items:baseline;padding:0 24px}
.step .num{font-size:30px;font-weight:500;color:#4b4d55}
.step h4{font-size:17px;font-weight:600}
.step.active{background:var(--panel);border-radius:12px;padding:24px;height:124px}
.step.active .num{color:var(--blue);font-weight:700}
.step.active p{font-size:13px;line-height:1.6;color:#9a9ca3;margin-top:8px;width:420px}
.step-panel{left:624px;top:340px;width:548px;height:408px;background:var(--panel);border-radius:16px;padding:40px}
.step-panel .big{font-size:86px;font-weight:700;color:#1a2d66;line-height:1}
.step-panel h3{font-size:28px;font-weight:600;margin:24px 0 14px}
.step-panel p{font-size:15px;line-height:1.6;color:#a3a5ab;width:420px}
.step-panel ul{list-style:none;margin-top:28px;font-size:14px;color:#cfd0d4}
.step-panel li{display:flex;align-items:center;gap:12px;margin-bottom:16px}
.step-panel li:before{content:"";width:6px;height:6px;border-radius:50%;background:var(--blue)}

/* about */
.about{top:5128px;height:844px}
.portrait{left:28px;top:120px;width:448px;height:600px;background:linear-gradient(180deg,#eceef0,#d9dce0 55%,#3a3f4a)}
.about-stats{left:120px;top:644px;width:380px;height:100px;background:var(--dark);border-radius:12px;display:flex;justify-content:space-around;align-items:center;color:var(--white);text-align:center}
.about-stats b{display:block;font-size:26px;color:#4d7cff}
.about-stats span{font-size:10px;color:var(--muted)}
.about-body{left:552px;top:192px;width:620px}
.about-body .h2{font-size:44px;margin:16px 0 28px}
.about-body p{font-size:14px;line-height:1.65;color:var(--text);margin-bottom:14px}
.about-body h5{font-size:13px;font-weight:700;margin:26px 0 14px}
.tags{display:flex;flex-wrap:wrap;gap:10px 12px;width:560px}
.tags span{font-size:12px;color:var(--text);border:1px solid var(--border);background:var(--card);padding:8px 14px;border-radius:18px}
.link{font-size:14px;font-weight:600;color:var(--blue);margin-top:28px}

/* testimonials */
.testimonials{top:5972px;height:688px;background:var(--soft)}
.arrows{left:28px;top:380px;display:flex;gap:36px;font-size:18px;color:var(--ink)}
.quote-card{left:328px;top:120px;width:844px;height:440px;background:var(--white);border-radius:16px;padding:56px 44px}
.quote-card blockquote{font-size:27px;line-height:1.7;color:#1e1f22;width:720px}
.quote-card .who{margin-top:40px;font-size:14px;font-weight:600}
.quote-card .who span{display:block;font-weight:400;color:var(--muted);margin-top:4px}
.quote-mark{right:32px;top:28px;width:50px;height:44px}
.dots{right:44px;bottom:64px;display:flex;gap:6px}
.dots i{width:8px;height:4px;border-radius:2px;background:#d6d8de;display:block}
.dots i.on{width:28px;background:var(--blue)}

/* contact */
.contact{top:6660px;height:704px}
.info{left:28px;width:532px;height:80px;border:1px solid var(--border);border-radius:12px;display:flex;align-items:center;gap:20px;padding:0 20px}
.info .ico{width:44px;height:44px;border-radius:10px;background:#eef2ff;display:flex;align-items:center;justify-content:center}
.info small{display:block;font-size:11px;color:var(--muted)}
.info b{font-size:14px;font-weight:600}
.form{left:636px;top:116px;width:536px;height:544px;background:var(--dark);border-radius:18px;padding:40px;color:var(--white)}
.form h3{font-size:24px;font-weight:600;margin-bottom:30px}
.field label{display:block;font-size:11px;font-weight:600;margin-bottom:8px}
.field div{height:46px;border-radius:8px;background:#1d1e22;border:1px solid #2c2d32;font-size:12px;color:#6a6d75;padding:14px 14px}
.row{display:flex;gap:16px;margin-bottom:20px}
.row .field{flex:1}
.form .btn-blue{display:block;text-align:center;margin-top:24px;padding:16px}

/* footer */
.footer{top:7364px;height:364px;background:var(--dark);color:var(--white)}
.footer p{font-size:13px;line-height:1.65;color:var(--muted)}
.fcol h6{font-size:14px;font-weight:600;margin-bottom:18px}
.fcol li{list-style:none;font-size:12px;color:var(--muted);margin-bottom:14px}
.fbottom{left:28px;right:28px;top:320px;display:flex;justify-content:space-between;font-size:11px;color:#6a6d75}
</style>
</head>
<body>
<div class="page">

  <section class="hero">
    <nav class="nav abs">
      <div class="brand"><span class="brand-dot"></span>valtro</div>
      <div class="nav-links"><span>Services</span><span>Portfolio</span><span>Process</span><span>About</span></div>
      <span class="nav-cta">Start a Project</span>
    </nav>
    <div class="hero-badge abs">● UK-Based Mechanical Design Consultancy</div>
    <h1 class="hero-title abs">We engineer<br><span class="accent">precision</span><br>into reality</h1>
    <p class="hero-copy abs">From concept to production-ready designs. We deliver bespoke mechanical engineering solutions that transform your ideas into manufacturable products.</p>
    <div class="hero-btns abs"><span class="btn-blue">Start Your Project &nbsp;→</span><span class="ghost">▷ &nbsp;View Our Work</span></div>
    <div class="stats abs">
      <div class="stat"><b>11+</b><span>Years Experience</span></div>
      <div class="stat"><b>100+</b><span>Projects Delivered</span></div>
      <div class="stat"><b>6+</b><span>Industries Served</span></div>
    </div>
    <div class="tablet abs"><div class="screen" role="img" aria-label="CAD software showing a 3D mechanical frame model"></div></div>
    <div class="float-card abs" style="left:972px;top:178px;width:196px"><i style="background:#2a3a70"></i><div>Design Approved<small>Ready for manufacture</small></div></div>
    <div class="float-card abs" style="left:612px;top:580px;width:204px"><i style="background:#1f5c3a"></i><div>Prototype Live<small>Testing in progress</small></div></div>
    <div class="industries abs">
      <p>TRUSTED ACROSS INDUSTRIES</p>
      <ul><li>Automotive</li><li>Medical Devices</li><li>Consumer Products</li><li>Industrial</li><li>Robotics</li><li>Aerospace</li></ul>
    </div>
  </section>

  <section class="services">
    <p class="label abs" style="left:28px;top:124px">What we do</p>
    <h2 class="h2 abs" style="left:28px;top:152px">Engineering services<br>that deliver</h2>
    <p class="lead abs" style="left:616px;top:196px;width:540px;font-size:15px">From initial concept sketches to production-ready designs, we provide comprehensive mechanical engineering solutions tailored to your specific requirements.</p>
    <div class="svc-grid abs">
      <div class="svc featured" style="grid-column:1;grid-row:1 / span 2">
        <div class="ico"><svg width="20" height="20" viewBox="0 0 20 20"><path d="M4 16 L16 4 M12 4h4v4" stroke="#4d7cff" stroke-width="2" fill="none"/></svg></div>
        <h3>Bespoke Product Design</h3><p>Innovative design from concept through the full development life cycle.</p><div class="tag">Featured Service</div>
      </div>
      <div class="svc" style="grid-column:2;grid-row:1">
        <div class="ico"><svg width="20" height="20" viewBox="0 0 20 20"><path d="M10 2 L17 6 V14 L10 18 L3 14 V6 Z M3 6 L10 10 L17 6 M10 10 V18" stroke="#1a56ff" stroke-width="1.6" fill="none"/></svg></div>
        <h3>3D CAD Modelling</h3><p>Comprehensive 3D CAD, 2D drawings, and photorealistic renders.</p>
      </div>
      <div class="svc" style="grid-column:3;grid-row:1">
        <div class="ico"><svg width="20" height="20" viewBox="0 0 20 20"><circle cx="10" cy="10" r="3" stroke="#1a56ff" stroke-width="1.6" fill="none"/><circle cx="10" cy="10" r="7" stroke="#1a56ff" stroke-width="1.6" stroke-dasharray="3 2" fill="none"/></svg></div>
        <h3>Design for Manufacture</h3><p>Designs optimised for prototype and production manufacture.</p>
      </div>
      <div class="svc featured" style="grid-column:2;grid-row:2 / span 2">
        <div class="ico"><svg width="20" height="20" viewBox="0 0 20 20"><circle cx="10" cy="10" r="6" stroke="#4d7cff" stroke-width="1.6" fill="none"/></svg></div>
        <h3>Mechanism Design</h3><p>Complex mechanical mechanism development and motion analysis.</p><div class="tag">Featured Service</div>
      </div>
      <div class="svc" style="grid-column:3;grid-row:2">
        <div class="ico"><svg width="20" height="20" viewBox="0 0 20 20"><path d="M5 15 L15 5 M7 3 L17 13" stroke="#1a56ff" stroke-width="1.6" fill="none"/></svg></div>
        <h3>Technical Documentation</h3><p>Complete drawing packages and manufacturing specifications.</p>
      </div>
      <div class="svc" style="grid-column:1;grid-row:3">
        <div class="ico"><svg width="20" height="20" viewBox="0 0 20 20"><circle cx="10" cy="10" r="6" stroke="#1a56ff" stroke-width="1.6" fill="none"/><circle cx="10" cy="10" r="2" fill="#1a56ff"/></svg></div>
        <h3>Prototype Development</h3><p>Rapid prototyping from 3D printing to CNC machining.</p>
      </div>
    </div>
  </section>

  <section class="projects">
    <p class="label abs" style="left:28px;top:124px">Our work</p>
    <h2 class="h2 abs" style="left:28px;top:152px;font-size:54px">Selected projects</h2>
    <div class="filters abs"><span class="on">All</span><span>Automotive</span><span>Industrial</span><span>Consumer Products</span></div>
    <div class="proj abs" style="left:28px;top:260px;width:560px;height:696px;background:radial-gradient(circle at 60% 50%,#e8e9eb,#9a9ca1 45%,#f4f4f5 75%)" role="img" aria-label="Chrome multi-spoke alloy wheel"><span class="chip">Automotive</span></div>
    <div class="proj abs" style="left:612px;top:260px;width:560px;height:416px;background:linear-gradient(180deg,#2a2c30,#4a4c52 60%,#1c1d20)" role="img" aria-label="Engineers inspecting machined metal parts in a workshop"><span class="chip">Industrial</span></div>
    <div class="proj abs" style="left:612px;top:700px;width:560px;height:420px;background:radial-gradient(circle at 50% 55%,#8a8c90,#3a3b3f 55%,#1e1f22)" role="img" aria-label="Metal hinge component render"><span class="chip">Consumer Products</span></div>
    <div class="proj abs" style="left:28px;top:1144px;width:560px;height:700px;background:linear-gradient(135deg,#f2f3f4,#d8dadd 60%,#bfc2c6)" role="img" aria-label="White medical device enclosure close-up"><span class="chip">Medical</span></div>
    <p class="more abs">View all projects &nbsp;→</p>
  </section>

  <section class="process">
    <p class="label abs" style="left:28px;top:124px">How we work</p>
    <h2 class="h2 abs" style="left:28px;top:152px">From concept to<br>production</h2>
    <p class="lead abs" style="left:616px;top:212px;width:540px;font-size:15px;color:#a3a5ab">A structured approach ensures quality results. Every project follows our proven five-stage process.</p>
    <div class="step active abs" style="top:340px"><span class="num">01</span><div><h4>Discovery</h4><p>We begin by understanding your project requirements, constraints, and objectives through detailed consultation.</p></div></div>
    <div class="step abs" style="top:500px"><span class="num">02</span><h4>Concept Development</h4></div>
    <div class="step abs" style="top:600px"><span class="num">03</span><h4>Detailed Design</h4></div>
    <div class="step abs" style="top:700px"><span class="num">04</span><h4>Prototyping</h4></div>
    <div class="step abs" style="top:800px"><span class="num">05</span><h4>Production Support</h4></div>
    <div class="step-panel abs">
      <div class="big">01</div>
      <h3>Discovery</h3>
      <p>We begin by understanding your project requirements, constraints, and objectives through detailed consultation.</p>
      <ul><li>Requirements analysis</li><li>Feasibility assessment</li><li>Project scoping</li></ul>
    </div>
  </section>

  <section class="about">
    <div class="portrait abs" role="img" aria-label="Portrait of the lead engineer in a suit"></div>
    <div class="about-stats abs">
      <div><b>11+</b><span>Years Experience</span></div>
      <div><b>100+</b><span>Projects Delivered</span></div>
      <div><b>6+</b><span>Industries Served</span></div>
    </div>
    <div class="about-body abs">
      <p class="label">About us</p>
      <h2 class="h2">Engineering expertise you<br>can trust</h2>
      <p>Valtro Mechanical Design is led by <b style="color:var(--ink)">Rowan Ellery</b>, a highly experienced mechanical design engineer with over a decade of expertise across multiple industries.</p>
      <p>Our consultancy bridges the gap between what management envisions and what manufacturing can deliver. With deep knowledge of casting processes and production techniques, we guide designs to produce excellent results every time.</p>
      <h5>Industry Expertise</h5>
      <div class="tags"><span>High Performance Automotive</span><span>Medical Devices</span><span>Consumer Products</span><span>Industrial Equipment</span><span>Robotics &amp; Automation</span><span>Aerospace Components</span></div>
      <p class="link">Work with us &nbsp;→</p>
    </div>
  </section>

  <section class="testimonials">
    <p class="label abs" style="left:28px;top:256px">Testimonials</p>
    <h2 class="h2 abs" style="left:28px;top:284px;font-size:32px">What our<br>clients say</h2>
    <div class="arrows abs"><span>‹</span><span>›</span></div>
    <div class="quote-card abs">
      <svg class="quote-mark abs" viewBox="0 0 50 44"><rect x="2" y="4" width="18" height="36" rx="4" fill="#e6ecff"/><rect x="28" y="4" width="18" height="36" rx="4" fill="#e6ecff"/></svg>
      <blockquote>“Rowan is able to bridge the gap between what management want and what manufacturing can deliver. In the field of Casting his intuition for the process and knowledge of casting technical nuances means he is able to push both the design and guide manufacturers to produce excellent results.”</blockquote>
      <p class="who">Martin Greave<span>Design Engineer</span></p>
      <div class="dots abs"><i class="on"></i><i></i><i></i></div>
    </div>
  </section>

  <section class="contact">
    <p class="label abs" style="left:28px;top:124px">Get in touch</p>
    <h2 class="h2 abs" style="left:28px;top:152px">Let's build<br>something great</h2>
    <p class="lead abs" style="left:28px;top:300px;width:540px;font-size:15px">Ready to bring your mechanical design project to life? Get in touch to discuss your requirements.</p>
    <div class="info abs" style="top:400px"><span class="ico"><svg width="18" height="18" viewBox="0 0 18 18"><rect x="2" y="4" width="14" height="10" rx="2" stroke="#1a56ff" stroke-width="1.5" fill="none"/><path d="M2 5 L9 10 L16 5" stroke="#1a56ff" stroke-width="1.5" fill="none"/></svg></span><div><small>Email us</small><b>info@valtrobuild.design</b></div></div>
    <div class="info abs" style="top:500px"><span class="ico"><svg width="18" height="18" viewBox="0 0 18 18"><path d="M4 2 L7 2 L8 6 L6 7 C7 9 9 11 11 12 L12 10 L16 11 L16 14 C16 15 15 16 14 16 C8 16 2 10 2 4 C2 3 3 2 4 2Z" stroke="#1a56ff" stroke-width="1.4" fill="none"/></svg></span><div><small>Call us</small><b>+44 (0) 7700 900418</b></div></div>
    <div class="info abs" style="top:600px"><span class="ico"><svg width="18" height="18" viewBox="0 0 18 18"><path d="M9 16 C9 16 3 10 3 7 A6 6 0 0 1 15 7 C15 10 9 16 9 16Z" stroke="#1a56ff" stroke-width="1.4" fill="none"/><circle cx="9" cy="7" r="2" fill="#1a56ff"/></svg></span><div><small>Location</small><b>United Kingdom</b></div></div>
    <div class="form abs">
      <h3>Start your project</h3>
      <div class="row"><div class="field"><label>Name</label><div>Your name</div></div><div class="field"><label>Email</label><div>your@email.com</div></div></div>
      <div class="row"><div class="field"><label>Company</label><div>Your company name</div></div></div>
      <div class="row"><div class="field"><label>Project Details</label><div style="height:56px">Tell us about your project...</div></div></div>
      <span class="btn-blue">Send Message &nbsp;→</span>
    </div>
  </section>

  <footer class="footer">
    <div class="brand abs" style="left:28px;top:52px"><span class="brand-dot"></span>valtro</div>
    <p class="abs" style="left:28px;top:112px;width:420px">UK-based mechanical design consultancy offering comprehensive engineering services from initial concepts through to full volume production.</p>
    <span class="abs" style="left:28px;top:212px;width:28px;height:28px;border-radius:6px;background:#2a2b30"></span>
    <div class="fcol abs" style="left:516px;top:52px"><h6>Services</h6><ul><li>Product Design</li><li>3D CAD Modelling</li><li>Design for Manufacture</li><li>Prototyping</li></ul></div>
    <div class="fcol abs" style="left:744px;top:52px"><h6>Company</h6><ul><li>About</li><li>Portfolio</li><li>Process</li><li>Contact</li></ul></div>
    <div class="fcol abs" style="left:972px;top:52px"><h6>Contact</h6><ul><li>info@valtrobuild.design</li><li>+44 (0) 7700 900418</li><li>United Kingdom</li></ul></div>
    <div class="fbottom abs"><span>© 2025 Valtro Mechanical Design. All rights reserved.</span><span>Valtro Build Ltd trading as Valtro Design. Registered in Wales. Company No. 14820397</span></div>
  </footer>

</div>
</body>
</html>
```